Flyer-Design für Neueröffnung eines Online-Shops
Zielgruppe
Ich verkaufe Online Lebensmittel, die normalerweise entsorgt werden, da das Mindesthaltbarkeitsdatum (MHD ) entweder in Kürze abläuft oder bereits überschritten ist, obwohl diese noch genießbar sind.
Der Fokus liegt auf nicht kühlbedürftige Ware wie Getränke, Süßwaren, Cerealien, Konserven, Gewürze, Getreidetrockenprodukte. Hinzu kommen Sonderposten aus Geschäftsauflösungen, Überproduktionen usw.
Das Ziel ist es, die Lebensmittelverschwendung zu reduzieren und der Bevölkerung, genießbare Lebensmittel zu einem geringen Preis anzubieten.
Die beiden Hauptzielgruppen sind;
1. Umweltbewusste Personen, die die Reduzierung der Lebensmittelverschwendung unterstützen wollen
2. Personen aus dem Niedriglohnsektor, die jeden Euro 'zweimal' umdrehen müssen und sich keine Markenware leisten können.
Aufgabenstellung
Der Onlineshop startet im Januar, das bedeutet der Onlineshop ist noch nicht bekannt. Daher soll der Flyer einem sofort ins Auge fallen. Jedoch soll auf dem Flyer nicht erwähnt werden, dass es sich um einen 'Neueröffnung' handelt.
Jedoch fahre ich eine Eröffnungsaktion, die jedoch als 'Januar' Special' oder Neujahrsspecial' o.ä. betitelt werden soll. Nämlich 'versandkostenfreie Lieferung ab 10€ Warenwert*'
*gilt für Bestellungen bis zum 31.01.18
Folgende Inhalte sollten im Design vorkommen:
Das Logo, der Slogan ' Verschwendung reduzieren, Ersparnis maximieren', die Domain 'www.kor-tibu.de' + der Hinweis auf die versandkostenfreie Lieferung am 10€ Warenwert im Januar.
Folgende Inhalte sind optional:
Stichwörter wie 'nachhaltig', 'umweltbewusst', 'bis zu 70% Ersparnis', '82kg Lebensmittel werden jährlich pro Person entsorgt',
Als Farbton sollte grün im Vordergrund stehen, gerne in zwei verschiedenen Helligkeitsstufen. Als Kontrastfarben wären Ideen rot( für den Rabatt/Ersparnis und da es sich um MHD nahe Lebensmittel handelt ) und schwarz oder weiß.
Der Flyer wird im A5 Hochformat gedruckt ( Querformat bei Bedarf auch möglich ). Dicke = voraussichtlich 300gr (alternativ 250gr ), 2-seitig
Ich werde das Logo und eine erste Skizze von einer Flyervorlage. Die Flyervorlage soll jedoch nur als Unterstützung für die Farbgebung dienen. Bitte die Designs unabhängig davon gestalten und diese evtl als kleine 'Hilfe' nutzen.
Da das Thema recht erklärungsbedürftig ist, ist meine Idee auf der Rückseite eine Art Begriffsklärung zu erstellen. Eine Vorlage für den Inhalt habe ich erstellt und wird ebenfalls hochgeladen. Jedoch soll die Begriffsklärung nicht einfach runtergeschrieben werden sondern kreativ eingebaut/verpackt werden ( z.B. Sprechblasen oder Emojis, Cliparts o.ä. )
Der Kunde soll sofort sehen, dass es darum geht die Lebensmittelverschwendung zu reduzieren und im gleichen Zuge genießb..

```html
<!DOCTYPE html>
<html lang="de">
<head>
<meta charset="utf-8">
<title>Kortibu – Flyer</title>
<link href="https://fonts.googleapis.com/css2?family=Arimo:wght@400;700&family=Archivo+Black&display=swap" rel="stylesheet">
<style>
  :root {
    --page-bg: #e6e6e4;
    --green-dark: #1e8a3e;
    --green-light: #6cc985;
    --green-text: #1f8a3c;
    --paper: #f3f3f1;
    --grey-band: #dcdcdc;
    --info-box: #e4e6e4;
    --red: #d82a2f;
    --black: #141414;
    --white: #ffffff;
  }
  html, body {
    margin: 0;
    width: 1200px;
    height: 900px;
    overflow: hidden;
    background: var(--page-bg);
  }
  .flyer {
    position: absolute;
    left: 300px;
    top: 26px;
    width: 600px;
    height: 848px;
    box-shadow: 0 6px 24px rgba(0,0,0,.18);
  }
  .flyer svg { display: block; width: 100%; height: 100%; }
  .txt { font-family: "Arimo", Arial, sans-serif; }
  .heavy { font-family: "Archivo Black", "Arial Black", sans-serif; }
  .white { fill: var(--white); }
  .green { fill: var(--green-text); }
</style>
</head>
<body>
<div class="flyer">
<svg viewBox="0 0 600 848" xmlns="http://www.w3.org/2000/svg">
  <defs>
    <linearGradient id="topGreen" x1="0" y1="0" x2="1" y2="1">
      <stop offset="0" stop-color="#34a24e"/>
      <stop offset="1" stop-color="#1f7f3a"/>
    </linearGradient>
    <linearGradient id="paperGrad" x1="0" y1="0" x2="0" y2="1">
      <stop offset="0" stop-color="#f7f7f5"/>
      <stop offset="1" stop-color="#e9e9e7"/>
    </linearGradient>
    <linearGradient id="logoArt" x1="0" y1="0" x2="1" y2="1">
      <stop offset="0" stop-color="#f4d9c4"/>
      <stop offset=".5" stop-color="#e8a23a"/>
      <stop offset="1" stop-color="#c9302c"/>
    </linearGradient>
    <clipPath id="sheet"><rect width="600" height="848"/></clipPath>
  </defs>

  <g clip-path="url(#sheet)">
    <!-- backgrounds -->
    <rect class="paper" width="600" height="848" fill="url(#paperGrad)"/>
    <rect class="top-band" width="600" height="370" fill="url(#topGreen)"/>

    <!-- logo circle -->
    <circle cx="200" cy="300" r="160" fill="var(--paper)"/>
    <circle class="logo-disc" cx="200" cy="300" r="140" fill="var(--green-dark)"/>

    <!-- savings bubble -->
    <g class="bubble-ring" fill="var(--paper)">
      <circle cx="478" cy="290" r="128"/>
      <polygon points="392,360 402,452 460,400"/>
    </g>
    <g class="bubble" fill="var(--green-light)">
      <circle cx="478" cy="290" r="115"/>
      <polygon points="404,365 410,432 456,395"/>
    </g>

    <!-- percentages -->
    <g class="txt white" font-weight="700">
      <text x="22" y="72" font-size="34">70%</text>
      <text x="112" y="58" font-size="28">60%</text>
      <text x="40" y="118" font-size="26">50%</text>
    </g>

    <!-- headline -->
    <g class="txt white" font-size="25" text-anchor="end">
      <text x="582" y="40">Der Onlineshop für MHD</text>
      <text x="582" y="70">nahe Lebensmittel</text>
      <text x="582" y="100">&amp; Sonderposten</text>
    </g>

    <!-- logo placeholder + name -->
    <rect x="110" y="200" width="180" height="110" rx="22" fill="url(#logoArt)" role="img" aria-label="Logo-Illustration: Lebensmittelpackungen mit grünem Haken"/>
    <text class="txt white" x="200" y="372" font-size="42" text-anchor="middle">Kortibu</text>

    <!-- bubble text -->
    <g class="txt white" font-weight="700" text-anchor="middle">
      <text x="478" y="250" font-size="32">Bis zu</text>
      <text x="478" y="318" font-size="66">70%</text>
      <text x="478" y="358" font-size="30">Ersparnis</text>
    </g>

    <!-- info box -->
    <rect x="318" y="460" width="268" height="56" fill="var(--info-box)"/>
    <g fill="none" stroke="var(--green-light)" stroke-width="3">
      <path d="M340 475 l-8 8 8 8 M350 475 l-8 8 8 8"/>
      <path d="M556 475 l8 8 -8 8 M566 475 l8 8 -8 8"/>
    </g>
    <g class="txt green" font-size="13" text-anchor="middle">
      <text x="452" y="483">82kg Lebensmittel werden</text>
      <text x="452" y="501">jährlich pro Person entsorgt</text>
    </g>

    <!-- feature icons -->
    <g fill="var(--white)" stroke="var(--green-text)" stroke-width="2.5">
      <polygon points="380,535 402,547 402,573 380,585 358,573 358,547"/>
      <polygon points="510,530 532,542 532,568 510,580 488,568 488,542"/>
    </g>
    <text class="txt green" x="380" y="568" font-size="24" font-weight="700" text-anchor="middle">€</text>
    <g fill="none" stroke="var(--green-text)" stroke-width="2">
      <path d="M502 548 h16 M506 548 v-3 h8 v3 M504 551 l2 18 h8 l2 -18"/>
    </g>
    <g class="txt green" font-size="12" font-weight="700" text-anchor="middle">
      <text x="380" y="603">Ersparnis</text>
      <text x="380" y="617">Maximieren</text>
      <text x="510" y="598">Verschwendung</text>
      <text x="510" y="612">Reduzieren</text>
    </g>

    <!-- product list -->
    <g class="txt green" font-size="24" font-weight="700">
      <rect x="22" y="478" width="13" height="13" fill="var(--green-text)"/><text x="44" y="492">Getränke</text>
      <rect x="22" y="511" width="13" height="13" fill="var(--green-text)"/><text x="44" y="525">Süßwaren</text>
      <rect x="22" y="544" width="13" height="13" fill="var(--green-text)"/><text x="44" y="558">Cerealien</text>
      <rect x="22" y="577" width="13" height="13" fill="var(--green-text)"/><text x="44" y="591">Konserven</text>
      <rect x="22" y="610" width="13" height="13" fill="var(--green-text)"/><text x="44" y="624">Gewürze</text>
      <rect x="22" y="643" width="13" height="13" fill="var(--green-text)"/><text x="44" y="657">Getreideprodukte</text>
    </g>

    <!-- offer band -->
    <rect class="offer-band" y="672" width="600" height="42" fill="var(--red)"/>
    <line x1="0" y1="677" x2="600" y2="677" stroke="#fff" stroke-width="1" stroke-dasharray="5 4" opacity=".7"/>
    <line x1="0" y1="709" x2="600" y2="709" stroke="#fff" stroke-width="1" stroke-dasharray="5 4" opacity=".7"/>
    <text class="heavy white" x="300" y="701" font-size="18" text-anchor="middle">Januar Special – AB 10€ VERSANKOSTENFREI</text>

    <!-- order band -->
    <rect class="order-band" y="714" width="600" height="56" fill="var(--grey-band)"/>
    <text class="heavy" x="300" y="752" font-size="28" fill="var(--black)" text-anchor="middle">Jetzt Online Bestellen</text>
    <g fill="none" stroke="var(--black)" stroke-width="3">
      <path d="M520 728 h7 l6 20 h20 l5 -14 h-28"/>
      <circle cx="536" cy="755" r="2.5" fill="var(--black)"/>
      <circle cx="550" cy="755" r="2.5" fill="var(--black)"/>
    </g>

    <!-- url band -->
    <rect class="url-band" y="770" width="600" height="78" fill="var(--black)"/>
    <text class="heavy white" x="300" y="823" font-size="40" text-anchor="middle" letter-spacing="2">www.kor-tibu.de</text>
  </g>
</svg>
</div>
</body>
</html>
```